I want to revise my business card design and get a more modern and up to date design.

uMendo Handyman Sevices originated from a family-owned and operated contractor business, performing home renovation, addition, and construction work in the NYC area since 2004. Today, we specialize in reliable and affordable handyman services for residential and commercial clients In 2014, we expanded to northern New Jersey. In 2016, we brought quality home improvement and repair services to new Bucks County, PA, and nearby New Jersey areas.
Target Market(s)
Home owners and business that might be looking for a General contractor, handyman, cleaning services and Home maintenance and property.
Industry/Entity Type
Construction Company
Contact Information for Business Card
I am open to new ideas
Colors
Designer to choose colors to be used in the design.
Look and feel

```html
<!DOCTYPE html>
<html lang="en">
<head>
<meta charset="utf-8">
<title>uMendo Handyman Services – Business Card</title>
<link href="https://fonts.googleapis.com/css2?family=Open+Sans:wght@400;600;700;800&display=swap" rel="stylesheet">
<style>
  :root {
    --stage: #1f2835;
    --red: #ec1c24;
    --black: #0b0b0b;
    --white: #ffffff;
    --grey: #4a4a4a;
    --yellow: #f7c928;
  }
  * { margin: 0; padding: 0; box-sizing: border-box; }
  html, body { width: 1000px; height: 1200px; overflow: hidden; }
  body {
    background: var(--stage);
    font-family: "Open Sans", Arial, sans-serif;
    position: relative;
  }
  .card {
    position: absolute;
    left: 175px;
    width: 625px;
    height: 357px;
    overflow: hidden;
  }
  .card-front { top: 133px; background: var(--black); }
  .card-back  { top: 720px; background: var(--white); }
  .card svg.card-art { position: absolute; inset: 0; width: 625px; height: 357px; }

  .wordmark {
    position: absolute;
    font-weight: 800;
    line-height: 1;
    letter-spacing: -1px;
  }
  .tagline {
    position: absolute;
    font-weight: 400;
    text-transform: uppercase;
    line-height: 1;
  }
  .card-front .brand-dot {
    position: absolute; left: 232px; top: 250px;
    width: 58px; height: 58px; border-radius: 50%;
    background: var(--white);
  }
  .card-front .wordmark { left: 312px; top: 240px; font-size: 70px; color: var(--white); }
  .card-front .tagline { left: 346px; top: 318px; font-size: 15px; letter-spacing: 3.4px; color: var(--white); }

  .card-back .wordmark { left: 28px; top: 62px; font-size: 58px; color: var(--black); }
  .card-back .tagline { left: 60px; top: 128px; font-size: 12.5px; letter-spacing: 2.6px; color: var(--grey); }

  .owner { position: absolute; right: 25px; top: 22px; text-align: right; }
  .owner-name { font-size: 24px; font-weight: 700; color: var(--black); line-height: 1.1; }
  .owner-role { font-size: 18px; font-weight: 700; color: var(--red); line-height: 1.1; }

  .contact { position: absolute; left: 24px; top: 218px; color: var(--white); }
  .contact-line { display: flex; align-items: center; gap: 8px; font-size: 19px; font-weight: 600; line-height: 28px; }
  .contact-line svg { width: 17px; height: 17px; flex: none; }
  .services { position: absolute; left: 24px; top: 284px; color: var(--red); text-transform: uppercase; line-height: 1; }
  .services-main { font-size: 25px; font-weight: 600; }
  .services-sub { font-size: 16.5px; font-weight: 700; margin-top: 6px; }
</style>
</head>
<body>

<section class="card card-front" aria-label="Business card front">
  <svg class="card-art" viewBox="0 0 625 357">
    <polygon points="0,0 465,0 465,70 395,200 330,357 0,357" fill="var(--red)" role="img" aria-label="Red honeycomb pattern of hexagons"/>
  </svg>
  <div class="brand-dot"></div>
  <div class="wordmark">umendo</div>
  <div class="tagline">Handyman Services</div>
</section>

<section class="card card-back" aria-label="Business card back">
  <svg class="card-art" viewBox="0 0 625 357">
    <polygon class="contact-band" points="0,205 330,205 400,165 400,150 515,88 627,150 627,357 0,357" fill="var(--black)"/>
    <defs>
      <linearGradient id="mascotTone" x1="0" y1="0" x2="0" y2="1">
        <stop offset="0" stop-color="var(--red)"/>
        <stop offset="0.45" stop-color="var(--yellow)"/>
        <stop offset="1" stop-color="var(--red)"/>
      </linearGradient>
    </defs>
    <polygon points="515,100 612,156 612,357 418,357 418,156" fill="url(#mascotTone)" role="img" aria-label="Mascot illustration of a lightbulb-headed handyman in a red cap and overalls"/>
  </svg>

  <div class="wordmark">umendo</div>
  <div class="tagline">Handyman Services</div>

  <div class="owner">
    <div class="owner-name">Rafael Moreira</div>
    <div class="owner-role">Owner</div>
  </div>

  <div class="contact">
    <div class="contact-line">
      <svg viewBox="0 0 24 24" aria-hidden="true"><path fill="var(--yellow)" d="M6.6 10.8a15.1 15.1 0 0 0 6.6 6.6l2.2-2.2c.3-.3.7-.4 1-.2 1.1.4 2.3.6 3.6.6.6 0 1 .4 1 1V20c0 .6-.4 1-1 1A17 17 0 0 1 3 4c0-.6.4-1 1-1h3.5c.6 0 1 .4 1 1 0 1.3.2 2.5.6 3.6.1.3 0 .7-.2 1z"/></svg>
      <span>(215) 555-0184</span>
    </div>
    <div class="contact-line">
      <svg viewBox="0 0 24 24" aria-hidden="true"><rect x="2" y="5" width="20" height="14" fill="var(--yellow)"/><path d="M2 5l10 8 10-8" fill="none" stroke="var(--black)" stroke-width="1.6"/></svg>
      <span>umendohandymannyc@email.com</span>
    </div>
  </div>

  <div class="services">
    <div class="services-main">Property Maintenance</div>
    <div class="services-sub">Cleaning and Handyman Services</div>
  </div>
</section>

</body>
</html>
```